Vantor Advisory business card

Premium business card required
I have attached the brand as a powerpoint template but this can be made to look very up market, I have also attached my BIO for title reasons and to give you a feel for my skills
front of card
Derek Holloway
Managing Director Vantor Advisory
Retail, Customer-Led Experience, Transformation and Maximising Shareholder Return
Mobile +61(0)418557392
Email derekvantoradvisory.com
back of card

VANTOR ADVISORY’ OFFERING

We transform customer environments to extract benefits while elevating service levels;
We release millions of dollars in self-funding through continuous improvement;
We see CX as a key differentiator, proactively guarding share from market disrupters;
We re-invent service and create front-end of the future.

```html
<!DOCTYPE html>
<html lang="en">
<head>
<meta charset="utf-8">
<title>Vantor Advisory Business Card</title>
<link href="https://fonts.googleapis.com/css2?family=Open+Sans:wght@400;600;700;800&display=swap" rel="stylesheet">
<style>
  :root {
    --backdrop: #2f2a27;
    --card: #151515;
    --card-edge: #0b0b0b;
    --logo-grey: #8a8a8a;
    --gold: #d8b23a;
    --text-light: #e9e9e9;
    --text-muted: #a9a9a9;
    --divider: #5a5a5a;
  }
  * { margin: 0; padding: 0; box-sizing: border-box; }
  html, body { width: 1200px; height: 864px; overflow: hidden; }
  body {
    background: var(--backdrop);
    font-family: "Open Sans", Arial, sans-serif;
    position: relative;
  }
  .card {
    position: absolute;
    width: 540px;
    height: 310px;
    background: var(--card);
    border-radius: 4px;
    box-shadow: 0 14px 30px rgba(0,0,0,0.55), 0 0 0 1px var(--card-edge);
  }
  .card-back { left: 40px; top: 120px; }
  .card-front { left: 620px; top: 420px; }

  .brand {
    display: flex;
    align-items: center;
    gap: 12px;
  }
  .brand-name {
    font-weight: 800;
    font-size: 30px;
    letter-spacing: 1px;
    color: var(--logo-grey);
    line-height: 1;
  }
  .brand-dot {
    flex: none;
    width: 30px; height: 30px;
    border-radius: 50%;
    background: var(--logo-grey);
  }

  .card-back .brand {
    position: absolute;
    left: 0; right: 0; top: 58px;
    justify-content: center;
  }
  .offering {
    position: absolute;
    left: 30px; right: 30px; top: 130px;
    text-align: center;
  }
  .offering-title {
    color: var(--gold);
    font-weight: 700;
    font-size: 14px;
    margin-bottom: 12px;
  }
  .offering-list { list-style: none; }
  .offering-list li {
    color: var(--text-muted);
    font-size: 10.5px;
    line-height: 1.6;
  }

  .card-front .brand {
    position: absolute;
    left: 30px; top: 122px;
    width: 180px;
  }
  .card-front .brand-name {
    font-size: 24px;
    line-height: 1.1;
  }
  .card-front .brand-dot { width: 26px; height: 26px; }
  .divider {
    position: absolute;
    left: 222px; top: 50px;
    width: 1px; height: 210px;
    background: linear-gradient(to bottom, transparent, var(--divider) 20%, var(--divider) 80%, transparent);
  }
  .person { position: absolute; left: 242px; top: 72px; right: 12px; }
  .person-name {
    color: var(--gold);
    font-weight: 700;
    font-size: 15px;
    letter-spacing: 0.5px;
    margin-bottom: 6px;
  }
  .person-role {
    color: var(--text-light);
    font-size: 10.5px;
    line-height: 1.45;
    margin-bottom: 12px;
    white-space: nowrap;
  }
  .contact-list { list-style: none; }
  .contact-list li {
    display: flex;
    align-items: center;
    gap: 8px;
    color: var(--text-light);
    font-size: 13px;
    line-height: 1.55;
    white-space: nowrap;
  }
  .contact-icon { width: 12px; height: 12px; flex: none; fill: var(--gold); }
</style>
</head>
<body>

  <section class="card card-back">
    <div class="brand">
      <span class="brand-name">VANTOR ADVISORY</span>
      <span class="brand-dot"></span>
    </div>
    <div class="offering">
      <h2 class="offering-title">Vantor Advisory Offering</h2>
      <ul class="offering-list">
        <li>We transform customer environments to extract benefits while elevating service levels;</li>
        <li>We release millions of dollars in self-funding through continuous improvement;</li>
        <li>We see CX as a key differentiator, proactively guarding share from market disrupters;</li>
        <li>We re-invent service and create front-end of the future.</li>
      </ul>
    </div>
  </section>

  <section class="card card-front">
    <div class="brand">
      <span class="brand-name">VANTOR<br>ADVISORY</span>
      <span class="brand-dot"></span>
    </div>
    <div class="divider"></div>
    <div class="person">
      <h1 class="person-name">DEREK HOLLOWAY</h1>
      <p class="person-role">Managing Director Vantor Advisory<br>Retail, Customer-Led Experience<br>Transformation &amp; Maximising Shareholder Return</p>
      <ul class="contact-list">
        <li>
          <svg class="contact-icon" viewBox="0 0 12 12" aria-hidden="true"><path d="M3 0h6a1 1 0 0 1 1 1v10a1 1 0 0 1-1 1H3a1 1 0 0 1-1-1V1a1 1 0 0 1 1-1zm0 1.5v8h6v-8z"/></svg>
          +61(0)418557392
        </li>
        <li>
          <svg class="contact-icon" viewBox="0 0 12 12" aria-hidden="true"><path d="M0 2h12v8H0zm1 1v.4l5 3.3 5-3.3V3z"/></svg>
          dh@derekvantoradvisory.com
        </li>
        <li>
          <svg class="contact-icon" viewBox="0 0 12 12" aria-hidden="true"><circle cx="6" cy="6" r="6"/></svg>
          derekvantoradvisory.com
        </li>
      </ul>
    </div>
  </section>

</body>
</html>
```